Toronto based adult novelty shop in need of website banners for new site

We are in need of a total of seven banners for our website.  We have one of Canada's largest selections of adult novelty items and fetish wear.  We have been serving the adult online community in Canada and the world since 2008.
There are two different sizes of banners needed.  The first measures 936px x 403px and feature products.  The other three banners measure  296px x 187px and highlight our customer policies.  The overall look we are going for should convey a sense of quality and elegance and should integrate with our new theme well.  You may view the test site by visiting http://velvetorchard.ca/testshop.  The banners displayed on the test site are placeholder graphics that came with the theme (not our banners or products).  Below is the list I've compiled for the content of the banners we need.  Product descriptions for the part numbers may be viewed by using the search box on our test website (see link above).
936 x 403 banner #1: Product number B938 Brass Tide Lubricant Copy should read something like: Brass Tide Silicone, Prepare for Action! (Military theme?)
936 x 403 banner #2: Product number AC245 Marigold Alloy Locking Anal Plug Copy should read something like: Add a new dimension to anal play
936 x 403 banner #3: Product number AB545 Leather and Brocade Nadia Corset Copy should read something like: Give your partner a visual feast
936 x 403 banner #4: Product number AD621 Orion Dusklight Premium Wand Kit Copy should read something like: Electrify your partner and light them up with this exceptional all-in-one set!
296 x 187 banner #1: Return Policy
Copy should read something like: Easy Returns, Don't like it?  Send it back! (click here for more information)
296 x 187 banner #2: Free Shipping
Copy should read something like: Free Expedited Shipping on orders over $149 (click here for details)
296 x 187 banner #3: Price Matching
Copy should read something like: We'll beat any price, online or anywhere else (some conditions and exclusions apply) I believe the disclaimers in parenthesis could be replaced by asterisk if it would look better.  I will link the images to the full terms.  I hope this is enough information for you.  Please feel free to take creative liberties and let me know if anything isn't working out the way I described.
I've attached image files for the products and also a screen shot of the site in case you cannot access it.

```html
<!DOCTYPE html>
<html lang="en">
<head>
<meta charset="utf-8">
<title>Velvet Orchard – Shop</title>
<link rel="stylesheet" href="https://fonts.googleapis.com/css2?family=Playfair+Display:wght@400;700&family=Ubuntu:wght@300;700&family=Arimo&display=swap">
<style>
  :root{
    --page:#f1f1f1;
    --white:#ffffff;
    --rule:#e2e2e2;
    --maroon:#6a0d2f;
    --nav-text:#8a8a8a;
    --caption:#9a9a9a;
    --banner-dark:#1a1a1a;
    --banner-mid:#2e2e2e;
    --silver:#c9c9c9;
    --note-box:#262626;
    --note-text:#a9a9a9;
    --title:#e8e8e8;
  }
  *{box-sizing:border-box;margin:0;padding:0}
  html,body{width:1200px;height:870px;overflow:hidden}
  body{background:var(--page);position:relative;font-family:"Playfair Display",serif}

  .site-header{position:absolute;left:0;top:0;width:1200px;height:113px;background:var(--white);border-bottom:1px solid var(--rule)}
  .brand-name{position:absolute;left:430px;top:28px;width:350px;text-align:center;font-family:"Playfair Display",serif;font-size:42px;font-weight:400;line-height:56px;color:var(--maroon)}

  .cart{position:absolute;left:904px;top:24px;display:flex;align-items:center}
  .cart-label{font-family:"Playfair Display",serif;font-size:12px;color:#222;margin-left:8px}
  .cart-caret{position:absolute;left:126px;top:20px;width:0;height:0;border-left:6px solid transparent;border-right:6px solid transparent;border-top:6px solid #c8c8c8}

  .main-nav{position:absolute;left:0;top:113px;width:1200px;height:50px;background:var(--white);border-bottom:1px solid var(--rule);box-shadow:0 3px 3px rgba(0,0,0,.04)}
  .nav-item{position:absolute;top:0;height:50px;border-left:1px solid var(--rule);border-right:1px solid var(--rule);font-family:"Playfair Display",serif;font-weight:700;font-size:16px;color:var(--nav-text);line-height:52px;padding-left:20px}
  .nav-item::after{content:"";position:absolute;right:10px;top:20px;border-left:5px solid transparent;border-right:5px solid transparent;border-top:6px solid #9a9a9a}
  .nav-home{left:134px;width:105px}
  .nav-help{left:238px;width:165px}
  .search-field{position:absolute;left:889px;top:0;width:148px;height:50px;border-left:1px solid var(--rule)}
  .search-button{position:absolute;left:1036px;top:0;width:48px;height:50px;border-left:1px solid var(--rule);border-right:1px solid var(--rule);display:flex;align-items:center;justify-content:center}

  .hero{position:absolute;left:134px;top:195px;width:950px;height:417px;background:var(--white)}
  .hero-banner{position:absolute;left:7px;top:7px;width:936px;height:403px;background:radial-gradient(ellipse at 50% 40%,var(--banner-mid),var(--banner-dark) 75%);overflow:hidden}
  .hero-banner::before,.hero-banner::after{content:"";position:absolute;left:0;width:936px;height:10px;background:linear-gradient(90deg,#9a9a9a,#f0f0f0 30%,var(--silver) 60%,#f4f4f4 85%,#9a9a9a)}
  .hero-banner::before{top:0}
  .hero-banner::after{bottom:0}
  .product-shot{position:absolute;left:8px;top:30px;width:400px;height:330px;border-radius:40% 30% 45% 35%;background:radial-gradient(ellipse at 45% 45%,#d8d8d8,#8d8d8d 45%,rgba(60,60,60,0) 72%)}
  .keys-shot{position:absolute;left:400px;top:300px;width:110px;height:75px;border-radius:40%;background:radial-gradient(ellipse,#9c9c9c,rgba(60,60,60,0) 70%)}
  .padlock-shot{position:absolute;left:856px;top:270px;width:62px;height:105px;border-radius:12px;background:linear-gradient(#b9b9b9 0 30%,#a88d3e 30%,#7a6527)}
  .hero-title{position:absolute;left:380px;top:28px;width:540px;text-align:center;font-family:"Ubuntu",sans-serif;font-weight:700;font-size:46px;line-height:49px;color:var(--title);text-shadow:0 2px 3px #000;letter-spacing:0.5px}
  .hero-rule{position:absolute;left:400px;top:141px;width:500px;height:1px;background:#555}
  .hero-sub{position:absolute;left:370px;top:144px;width:560px;text-align:center;font-family:"Ubuntu",sans-serif;font-weight:300;font-size:32px;color:#f2f2f2}
  .hero-note{position:absolute;height:59px;background:var(--note-box);font-family:"Arimo",sans-serif;font-size:20px;line-height:20px;color:var(--note-text);text-align:center;padding-top:9px}
  .note-lock{left:453px;top:203px;width:402px}
  .note-handle{left:450px;top:279px;width:404px}

  .policy{position:absolute;top:622px;width:310px;height:201px;background:var(--white)}
  .policy-card{position:absolute;left:7px;top:7px;width:296px;height:187px;border:1px solid #dcdcdc;background:radial-gradient(ellipse at 50% 40%,#ffffff,#ececec 90%);color:var(--maroon);font-family:"Playfair Display",serif}
  .policy-returns{left:134px}
  .policy-shipping{left:454px}
  .policy-price{left:774px}
  .policy-card > div{position:absolute;left:0;width:294px;text-align:center;white-space:nowrap}
  .policy-big{font-size:64px;line-height:64px;font-weight:700}
  .policy-mid{font-size:32px;line-height:38px;font-weight:700;letter-spacing:-0.5px}
  .policy-small{font-size:23px;line-height:30px;font-weight:700;letter-spacing:-0.3px}
  .policy-caption{font-size:17px;line-height:22px;color:var(--caption);font-weight:700;letter-spacing:-0.3px}
</style>
</head>
<body>
  <header class="site-header">
    <div class="brand-name">Velvet Orchard</div>
    <div class="cart">
      <svg width="34" height="46" viewBox="0 0 34 46" aria-hidden="true">
        <path d="M3 12 L30 10 L32 42 L5 44 Z" fill="#fafafa" stroke="#cfcfcf"/>
        <path d="M12 12 C12 2 22 2 22 11" fill="none" stroke="#aaa" stroke-width="1.2"/>
      </svg>
      <span class="cart-label">EMPTY</span>
      <span class="cart-caret"></span>
    </div>
  </header>

  <nav class="main-nav">
    <div class="nav-item nav-home">HOME</div>
    <div class="nav-item nav-help">HELP &amp; INFO</div>
    <div class="search-field"></div>
    <div class="search-button">
      <svg width="14" height="14" viewBox="0 0 14 14" aria-label="Search">
        <circle cx="6" cy="6" r="4.5" fill="none" stroke="#444" stroke-width="2"/>
        <line x1="9.5" y1="9.5" x2="13" y2="13" stroke="#444" stroke-width="2"/>
      </svg>
    </div>
  </nav>

  <section class="hero">
    <div class="hero-banner">
      <div class="product-shot" role="img" aria-label="Polished steel locking anal plug with T-bar handle and expanded petals"></div>
      <div class="keys-shot" role="img" aria-label="Two small keys"></div>
      <div class="padlock-shot" role="img" aria-label="Brass padlock"></div>
      <h1 class="hero-title">MARIGOLD ALLOY<br>LOCKING ANAL PLUG</h1>
      <div class="hero-rule"></div>
      <p class="hero-sub">Add a new dimension to anal play!</p>
      <p class="hero-note note-lock">Use the lock and key to keep the<br>fully expanded plug in place.</p>
      <p class="hero-note note-handle">The bar handle allows for easy grip and<br>manipulation of plug's position.</p>
    </div>
  </section>

  <section class="policy policy-returns">
    <div class="policy-card">
      <div class="policy-big" style="top:17px">easy</div>
      <div class="policy-mid" style="top:93px">RETURNS</div>
      <div class="policy-caption" style="top:151px">DON'T LIKE IT? SEND IT BACK!</div>
    </div>
  </section>

  <section class="policy policy-shipping">
    <div class="policy-card">
      <div class="policy-big" style="top:14px">free</div>
      <div class="policy-mid" style="top:73px">EXPEDITED<br>SHIPPING</div>
      <div class="policy-caption" style="top:151px">ON ORDERS OVER $149</div>
    </div>
  </section>

  <section class="policy policy-price">
    <div class="policy-card">
      <div class="policy-big" style="top:16px">price</div>
      <div class="policy-mid" style="top:75px;line-height:34px;padding-left:18px;text-transform:none">matching</div>
      <div class="policy-small" style="top:117px">WE'LL BEAT ANY PRICE!</div>
      <div class="policy-caption" style="top:151px">SOME CONDITIONS APPLY</div>
    </div>
  </section>
</body>
</html>
```